Borealis Film and Design
Your Moments on Reels
Borealis Film and Design -
Creative Brief
Professional
Peter Vandrell
2187 Kettering Ln. Frostmere, Northland 99612
Peter@borealisfilmanddesign.example
borealisfilmanddesign.example

```html
<!DOCTYPE html>
<html lang="en">
<head>
<meta charset="utf-8">
<title>Borealis Film and Design – Business Card</title>
<link rel="stylesheet" href="https://fonts.googleapis.com/css2?family=Montserrat:wght@500;800&family=Open+Sans:wght@400&display=swap">
<style>
  :root {
    --page-bg: #e9e6e1;
    --card-white: #ffffff;
    --band-dark: #0d1460;
    --band-mid: #1f3aa8;
    --band-bright: #2f6fe0;
    --name-blue: #3a3aa0;
    --ink: #2b2b2b;
    --logo-ink: #1c2b7a;
    --divider: #9a9a9a;
  }
  * { box-sizing: border-box; margin: 0; padding: 0; }
  html, body { width: 1200px; height: 799px; overflow: hidden; }
  body {
    background: var(--page-bg);
    font-family: "Open Sans", Arial, sans-serif;
    position: relative;
  }
  .business-card {
    position: absolute;
    left: 100px; top: 116px;
    width: 1000px; height: 567px;
    background: var(--card-white);
    border-radius: 28px;
    overflow: hidden;
    box-shadow: 0 6px 18px rgba(0,0,0,0.18);
  }
  .band {
    position: absolute; left: 0; width: 100%;
    background: linear-gradient(90deg, var(--band-mid) 0%, var(--band-bright) 40%, var(--band-dark) 100%);
  }
  .band--top { top: 0; height: 72px; }
  .band--bottom { bottom: 0; height: 66px; display: flex; align-items: center; justify-content: center; }
  .rule {
    position: absolute; left: 0; width: 100%; height: 6px;
    background: linear-gradient(90deg, var(--band-mid), var(--band-dark));
  }
  .rule--top { top: 82px; }
  .rule--bottom { bottom: 76px; }
  .website {
    color: #fff; font-size: 22px; letter-spacing: 5px;
  }
  .brand {
    position: absolute; top: 160px; left: 0; width: 100%;
    display: flex; align-items: center; justify-content: center; gap: 18px;
  }
  .brand-dot { width: 38px; height: 38px; border-radius: 50%; background: var(--band-bright); flex: none; }
  .brand-name {
    font-family: "Montserrat", Arial, sans-serif; font-weight: 800;
    font-size: 50px; line-height: 1; color: var(--logo-ink); letter-spacing: 1px;
  }
  .person-name {
    position: absolute; left: 64px; top: 368px;
    font-family: "Montserrat", Arial, sans-serif; font-weight: 500;
    font-size: 28px; line-height: 1; letter-spacing: 2px; color: var(--name-blue);
    text-transform: uppercase;
  }
  .divider {
    position: absolute; left: 375px; top: 298px;
    width: 1px; height: 168px; background: var(--divider);
  }
  .contact {
    position: absolute; left: 412px; top: 318px;
    font-size: 21px; line-height: 33px; color: var(--ink);
    list-style: none;
  }
  .contact li { display: flex; align-items: center; gap: 9px; white-space: nowrap; }
  .contact svg { width: 17px; height: 17px; flex: none; }
</style>
</head>
<body>
  <div class="business-card">
    <div class="band band--top"></div>
    <div class="rule rule--top"></div>

    <div class="brand">
      <span class="brand-dot"></span>
      <span class="brand-name">Borealis Film and Design</span>
    </div>

    <p class="person-name">Peter Vandrell</p>
    <div class="divider"></div>
    <ul class="contact">
      <li>2187 Kettering Ln.</li>
      <li>Frostmere, Northland 99612</li>
      <li>
        <svg viewBox="0 0 16 16" aria-hidden="true"><rect x="4" y="1" width="8" height="14" rx="2" fill="#1f3aa8"/><rect x="5.5" y="3" width="5" height="8" fill="#fff"/></svg>
        1-907-555-0186
      </li>
      <li>
        <svg viewBox="0 0 16 16" aria-hidden="true"><rect x="1" y="3" width="14" height="10" rx="1" fill="#1f3aa8"/><path d="M1.5 4 8 9l6.5-5" stroke="#fff" stroke-width="1.4" fill="none"/></svg>
        Peter@borealisfilmanddesign.example
      </li>
    </ul>

    <div class="rule rule--bottom"></div>
    <div class="band band--bottom">
      <span class="website">www.borealisfilmanddesign.example</span>
    </div>
  </div>
</body>
</html>
```